KVD Insurance - Letterhead

We need a corporate letterhead template (word) and slide show template (PowerPoint) designed for our Insurance Business.
KVD Insurance is in the insurance industry. Please visit our website www.kvdinsurance-example.com
Both templates (word and PowerPoint) must include the KVD logo (attached to this project) and can be very similar in design.
We are after something creative yet professional in design.
Please feel free to ask any questions.

```html
<!DOCTYPE html>
<html lang="en">
<head>
<meta charset="utf-8">
<title>KVD Insurance – Letterhead</title>
<link rel="stylesheet" href="https://fonts.googleapis.com/css2?family=Mulish:wght@200;300;400;700&display=swap">
<style>
  :root {
    --ink: #2b2b2b;
    --brand-orange: #e4502a;
    --brace-grey: #b5b5b5;
    --paper: #ffffff;
    --stripe-salmon: #f2a58e;
    --stripe-yellow: #f7e08e;
    --stripe-lavender: #a8a3cf;
  }
  html, body {
    margin: 0;
    padding: 0;
    overflow: hidden;
    background: var(--paper);
  }
  .letterhead {
    position: relative;
    width: 847px;
    height: 1200px;
    overflow: hidden;
    background: var(--paper);
    font-family: "Mulish", sans-serif;
    color: var(--ink);
  }
  .brand {
    position: absolute;
    left: 56px;
    top: 84px;
    display: flex;
    align-items: center;
    gap: 12px;
  }
  .brand-dot {
    width: 26px;
    height: 26px;
    border-radius: 50%;
    background: var(--brand-orange);
  }
  .brand-name {
    font-weight: 700;
    font-size: 30px;
    letter-spacing: 1px;
    color: var(--ink);
  }
  .contact-list {
    position: absolute;
    right: 88px;
    top: 60px;
    margin: 0;
    padding: 0;
    list-style: none;
    text-align: right;
    font-size: 13.5px;
    font-weight: 400;
  }
  .contact-list li {
    height: 20px;
    line-height: 20px;
  }
  .contact-list li + li { margin-top: 22px; }
  .contact-tab {
    position: absolute;
    left: 772px;
    top: 0;
    width: 39px;
    height: 180px;
    background: var(--brand-orange);
    border-radius: 0 0 14px 14px;
  }
  .contact-tab svg {
    position: absolute;
    left: 10px;
    width: 19px;
    height: 19px;
  }
  .title-block {
    position: absolute;
    left: 0;
    top: 0;
    width: 100%;
    height: 100%;
    color: var(--brace-grey);
    font-weight: 200;
  }
  .brace-open {
    position: absolute;
    left: 160px;
    top: 392px;
    font-size: 330px;
    line-height: 1;
  }
  .brace-close {
    position: absolute;
    left: 582px;
    top: 520px;
    font-size: 150px;
    line-height: 1;
  }
  .title-text {
    position: absolute;
    left: 259px;
    top: 565px;
    font-size: 40px;
    font-weight: 300;
    color: var(--ink);
    letter-spacing: 0.2px;
  }
  .registration {
    position: absolute;
    left: 0;
    width: 100%;
    top: 1138px;
    text-align: center;
    font-size: 13.5px;
  }
  .footer-stripes {
    position: absolute;
    left: 0;
    bottom: 0;
    width: 100%;
  }
  .footer-stripes div { height: 6px; }
  .stripe-salmon { background: var(--stripe-salmon); }
  .stripe-yellow { background: var(--stripe-yellow); }
  .stripe-lavender { background: var(--stripe-lavender); }
</style>
</head>
<body>
<main class="letterhead">
  <header>
    <div class="brand">
      <span class="brand-dot"></span>
      <span class="brand-name">KVD Insurance</span>
    </div>

    <ul class="contact-list">
      <li>Po Box 718, Northvale VIC 3190</li>
      <li>1300 555 018</li>
      <li>info@kvdinsurance-example.com</li>
    </ul>

    <div class="contact-tab">
      <svg style="top:52px" viewBox="0 0 24 24" aria-hidden="true">
        <path fill="#fff" d="M12 2a7 7 0 0 0-7 7c0 5 7 13 7 13s7-8 7-13a7 7 0 0 0-7-7zm0 9.5A2.5 2.5 0 1 1 12 6.5a2.5 2.5 0 0 1 0 5z"/>
      </svg>
      <svg style="top:97px" viewBox="0 0 24 24" aria-hidden="true">
        <path fill="#fff" d="M6.6 10.8a15 15 0 0 0 6.6 6.6l2.2-2.2a1 1 0 0 1 1-.25 11.4 11.4 0 0 0 3.6.57 1 1 0 0 1 1 1V20a1 1 0 0 1-1 1A17 17 0 0 1 3 4a1 1 0 0 1 1-1h3.5a1 1 0 0 1 1 1c0 1.25.2 2.45.57 3.6a1 1 0 0 1-.25 1z"/>
      </svg>
      <svg style="top:137px" viewBox="0 0 24 24" aria-hidden="true">
        <rect x="3" y="5" width="18" height="14" fill="none" stroke="#fff" stroke-width="1.8"/>
        <path d="M3 5l9 8 9-8M3 19l6.5-6.5M21 19l-6.5-6.5" fill="none" stroke="#fff" stroke-width="1.8"/>
      </svg>
    </div>
  </header>

  <section class="title-block">
    <span class="brace-open">{</span>
    <h1 class="title-text" style="margin:0">letterhead design</h1>
    <span class="brace-close">}</span>
  </section>

  <footer>
    <p class="registration" style="margin:0">ABN: 00 123 456 789 &amp; FSL: 000 000.</p>
    <div class="footer-stripes">
      <div class="stripe-salmon"></div>
      <div class="stripe-yellow"></div>
      <div class="stripe-lavender"></div>
    </div>
  </footer>
</main>
</body>
</html>
```